10 Page Marketing Report Template - Quillmont Care Associates

https://www.vexaclip.com/view/8f1d2e7b90c44a6f81e2d3b5c7a9f014

We are creating a professional, modern, and slightly edgy PDF-style report document (about 10 pages) to showcase the results of a client’s first 30 days with Quillmont Care Associates.

The report will be designed as a customizable Canva template so the Client Success team can easily update logos, screenshots, and text for each client.

This document will serve as both a visual presentation piece and a report deliverable, blending clean design, modern layout, and data-driven storytelling.

I am attaching the content for the report doc and the design brief along with the logo.
Here is our website for design style, look, and feel: https://quillmontcare.example/

Here is a quick overview video I made:

```html
<!DOCTYPE html>
<html lang="en">
<head>
<meta charset="utf-8">
<title>30 Days to Value Report – Quillmont Care Associates</title>
<link rel="stylesheet" href="https://fonts.googleapis.com/css2?family=Poppins:ital,wght@0,400;0,500;0,600;0,700;1,400&display=swap">
<style>
:root{
  --bg:#d0d0d0;
  --navy:#1b2540;
  --navy-deep:#10182c;
  --teal:#0f4766;
  --gold:#fbb40f;
  --ink:#1e1e1e;
  --muted:#5b5b5b;
  --paper:#ffffff;
  --placeholder:#efefef;
}
*{box-sizing:border-box;margin:0;padding:0}
html,body{width:696px;height:1200px;overflow:hidden;background:var(--bg)}
body{font-family:"Poppins",sans-serif;color:var(--ink)}
.sheet{position:relative;width:1461px;height:2520px;transform:scale(.47638);transform-origin:0 0}
.page{position:absolute;width:379px;height:536px;background:var(--paper);overflow:hidden}
.abs{position:absolute}

/* cover */
.cover{left:541px;top:120px}
.cover-photo{position:absolute;left:0;top:0;width:379px;height:426px;background:radial-gradient(ellipse at 75% 70%,#2c3852 0%,#19223a 45%,#0d1427 100%)}
.cover-rule{position:absolute;left:0;top:426px;width:379px;height:4px;background:var(--gold)}
.cover-motto{position:absolute;top:45px;width:100%;text-align:center;color:#fff;font-weight:600;font-size:14px;line-height:16px}
.cover-motto .hl{color:var(--gold)}
.cover-swoosh{position:absolute;left:165px;top:102px}
.cover-title{position:absolute;top:143px;width:100%;text-align:center;font-weight:700;font-size:44px;line-height:42px;color:#fff;letter-spacing:.5px}
.cover-title .hl{color:var(--gold)}
.cover-sub{position:absolute;top:316px;width:100%;text-align:center;color:#fff;font-size:10.5px;font-weight:500}
.cover-meta{position:absolute;left:120px;color:#fff;font-size:6.5px}
.cover-meta b{font-weight:600}
.cover-logo{position:absolute;left:0;top:474px;width:100%;display:flex;align-items:center;justify-content:center;gap:7px}
.cover-logo .mark{width:11px;height:11px;background:var(--gold)}
.cover-logo .name{color:var(--navy);font-weight:600;font-size:12px;line-height:14px}

/* inner page frame */
.band{position:absolute;left:0;top:0;width:379px;height:56px;background:linear-gradient(90deg,#1a2238,#232d47 60%,#1a2238)}
.band-title{position:absolute;left:21px;top:13px;font-weight:700;font-size:15px;line-height:15px;color:#fff;opacity:.14;text-transform:uppercase}
.band-rule{position:absolute;left:0;top:56px;width:379px;height:3px;background:var(--gold)}
.foot-logo{position:absolute;left:22px;top:503px;display:flex;align-items:center;gap:4px}
.foot-logo .mark{width:6px;height:6px;background:var(--gold)}
.foot-logo .name{color:var(--navy);font-weight:600;font-size:6px;line-height:7px;white-space:nowrap}
.page-no{position:absolute;left:345px;top:508px;width:11px;height:28px;background:var(--navy);color:#fff;font-size:5px;text-align:center;padding-top:3px}

/* text */
.title{position:absolute;left:22px;top:78px;font-weight:700;font-size:14.5px;line-height:15px;text-transform:uppercase;color:var(--navy)}
.title .hl{color:var(--gold)}
.para{position:absolute;left:22px;width:335px;font-size:6.8px;line-height:8.4px;text-align:justify}
.sub{position:absolute;left:22px;font-weight:600;font-size:9px;line-height:10px;color:var(--gold);text-transform:uppercase}
.sub .dk{color:var(--navy)}
.sub.cap{text-transform:none}
.list{position:absolute;left:22px;list-style:none;font-size:6.8px}
.list li{position:relative;padding-left:11px;margin-bottom:7.2px;line-height:8px}
.list li::before{content:"";position:absolute;left:2px;top:3px;width:2.4px;height:2.4px;border-radius:50%;background:var(--ink)}
.list.wide{width:335px;text-align:justify}
.defs{position:absolute;left:22px;font-size:6.8px;line-height:13.6px}
.defs b{font-weight:600}
.caption{position:absolute;left:22px;width:335px;font-size:6.8px;font-style:italic;line-height:8.4px;text-align:justify}
.bracket{position:absolute;left:22px;font-size:6.8px}
.photo{position:absolute}
.ph-box{position:absolute;background:var(--placeholder);color:#d0d0d0;font-size:5.5px;display:flex;align-items:center;justify-content:center}
</style>
</head>
<body>
<main class="sheet">

  <section class="page cover">
    <div class="cover-photo" role="img" aria-label="Team meeting around a conference table under a dark navy tint"></div>
    <div class="cover-rule"></div>
    <p class="cover-motto">Live With Integrity.<br><span class="hl">Serve With Excellence.</span><br>Change The World.</p>
    <svg class="cover-swoosh" width="50" height="26" viewBox="0 0 50 26"><path d="M2 24 Q24 16 44 4" stroke="var(--gold)" stroke-width="2.4" fill="none" stroke-linecap="round"/><path d="M38 3 L46 2 L42 9 Z" fill="var(--gold)"/></svg>
    <h1 class="cover-title">30<br>DAYS TO<br><span class="hl">VALUE<br>REPORT</span></h1>
    <p class="cover-sub">Quillmont Care Associates</p>
    <p class="cover-meta" style="top:375px"><b>Client:</b> [Client Name] &nbsp;&nbsp;&nbsp;<b>Date:</b> 22-11-2025</p>
    <p class="cover-meta" style="top:388px"><b>Prepared by:</b> Quillmont Care Associates</p>
    <div class="cover-logo"><span class="mark"></span><span class="name">Quillmont Care Associates</span></div>
  </section>

  <section class="page" style="left:120px;top:701px">
    <div class="band"></div><p class="band-title">30 Days to<br>Value Report</p><div class="band-rule"></div>
    <h2 class="title"><span class="hl">Welcome</span><br>And Overview</h2>
    <p class="para" style="top:118px">The first 30 days are about creating momentum. Our goal was to build the foundation for measurable growth — from your website and Findwell Business Profile to your SEO systems, audits, and backlink strategy.</p>
    <div class="photo" style="left:22px;top:156px;width:335px;height:144px;background:linear-gradient(135deg,#2a3140,#6b7688 55%,#c9ced6)" role="img" aria-label="Business partners shaking hands at a meeting table"></div>
    <p class="caption" style="top:309px">This report highlights what’s been accomplished and what’s next in your marketing journey.</p>
    <div class="foot-logo"><span class="mark"></span><span class="name">Quillmont Care Associates</span></div>
    <div class="page-no">01</div>
  </section>

  <section class="page" style="left:541px;top:701px">
    <div class="band"></div><p class="band-title">30 Days to<br>Value Report</p><div class="band-rule"></div>
    <h2 class="title"><span class="hl">Highlights</span><br>And Quick Wins</h2>
    <ul class="list" style="top:121px">
      <li>Website launched and optimized for SEO</li>
      <li>Findwell Business Profiles verified and optimized</li>
      <li>Comprehensive SEO audits completed</li>
      <li>Backlink strategy implementation underway</li>
      <li>First blog articles published</li>
      <li>Tracking and analytics systems connected</li>
    </ul>
    <div class="photo" style="left:22px;top:217px;width:335px;height:144px;background:linear-gradient(135deg,#5b6068,#9aa0a8 50%,#3d4148)" role="img" aria-label="Hand sketching 2025 with upward arrows in chalk"></div>
    <div class="foot-logo"><span class="mark"></span><span class="name">Quillmont Care Associates</span></div>
    <div class="page-no">01</div>
  </section>

  <section class="page" style="left:962px;top:701px">
    <div class="band"></div><p class="band-title">30 Days to<br>Value Report</p><div class="band-rule"></div>
    <h2 class="title"><span class="hl">Comprehensive Audits</span><br>And Strategy Development</h2>
    <p class="para" style="top:118px">To ensure long-term results, our team conducted a full suite of technical and strategic audits during the first month. These insights guided your SEO roadmap and content strategy moving forward.</p>
    <p class="sub" style="top:161px">Audits and<br><span class="dk">Deliverables Completed:</span></p>
    <p class="defs" style="top:185px">
      <b>Technical SEO Audit:</b> Site health, indexation, and crawl efficiency<br>
      <b>Backlink Audit:</b> Link quality, toxicity review, and authority scoring<br>
      <b>Competitor Analysis:</b> Top-ranking competitors’ content, backlinks, and keyword profiles<br>
      <b>On-Page SEO Audit:</b> Metadata, headings, internal links, and content structure<br>
      <b>Content Audit:</b> Keyword targeting, topical gaps, and conversion opportunities<br>
      <b>Strategy Development:</b> 90-day SEO plan and keyword roadmap created
    </p>
    <div class="ph-box" style="left:22px;top:279px;width:161px;height:111px">PLACE HOLDER</div>
    <div class="ph-box" style="left:194px;top:279px;width:161px;height:111px">PLACE HOLDER</div>
    <div class="foot-logo"><span class="mark"></span><span class="name">Quillmont Care Associates</span></div>
    <div class="page-no">01</div>
  </section>

  <section class="page" style="left:120px;top:1283px">
    <div class="band"></div><p class="band-title">30 Days to<br>Value Report</p><div class="band-rule"></div>
    <h2 class="title"><span class="hl">Website</span><br>Progress</h2>
    <p class="para" style="top:118px">To ensure long-term results, our team conducted a full suite of technical and strategic audits during the first month. These insights guided your SEO roadmap and content strategy moving forward.</p>
    <p class="sub" style="top:172px">Launched Pages</p>
    <p class="bracket" style="top:186px">[List live pages, e.g., Home, About, Services, Contact, etc.]</p>
    <svg class="abs" style="left:255px;top:166px" width="90" height="124" viewBox="0 0 90 124">
      <rect x="4" y="2" width="82" height="118" rx="4" fill="#111"/>
      <rect x="8" y="7" width="74" height="108" fill="#fff"/>
      <rect x="18" y="58" width="4" height="4" fill="var(--gold)"/>
      <text x="25" y="61.5" font-family="Poppins,sans-serif" font-size="4" font-weight="600" fill="var(--navy)">Quillmont Care Associates</text>
    </svg>
    <p class="sub" style="top:240px">Optimizations Completed</p>
    <ul class="list" style="top:254px">
      <li>On-page SEO (titles, meta, H1s)</li>
      <li>Local schema added</li>
      <li>Call tracking integrated</li>
      <li>Mobile responsiveness reviewed</li>
    </ul>
    <svg class="abs" style="left:208px;top:306px" width="150" height="88" viewBox="0 0 150 88">
      <rect x="16" y="2" width="118" height="78" rx="3" fill="#111"/>
      <rect x="20" y="6" width="110" height="70" fill="#fff"/>
      <rect x="2" y="80" width="146" height="4" rx="2" fill="#c8c8c8"/>
      <rect x="50" y="36" width="4" height="4" fill="var(--gold)"/>
      <text x="57" y="39.5" font-family="Poppins,sans-serif" font-size="4" font-weight="600" fill="var(--navy)">Quillmont Care Associates</text>
    </svg>
    <p class="sub" style="top:358px">Next Steps</p>
    <ul class="list" style="top:372px">
      <li>CRO improvements</li>
      <li>Additional service or location pages</li>
    </ul>
    <div class="foot-logo"><span class="mark"></span><span class="name">Quillmont Care Associates</span></div>
    <div class="page-no">01</div>
  </section>

  <section class="page" style="left:541px;top:1283px">
    <div class="band"></div><p class="band-title">30 Days to<br>Value Report</p><div class="band-rule"></div>
    <h2 class="title"><span class="hl">Findwell</span><br>Business Profile</h2>
    <ul class="list" style="top:120px">
      <li>Profiles verified and optimized</li>
      <li>Categories, services, and photos updated</li>
      <li>Images updated and optimized for visibility and engagement</li>
      <li>Review strategy initiated</li>
      <li>Visibility and engagement tracking started</li>
    </ul>
    <div class="photo" style="left:22px;top:207px;width:95px;height:186px;border:2px solid #d6d6d6;border-radius:8px;background:linear-gradient(90deg,#fff 68%,#dfe6df)" role="img" aria-label="Phone screen showing the profile menu"></div>
    <div class="photo" style="left:141px;top:207px;width:95px;height:186px;border:2px solid #d6d6d6;border-radius:8px;background:linear-gradient(160deg,#e4ebe4,#cfd8d1 50%,#e8ece8)" role="img" aria-label="Phone screen showing a map with location pins"></div>
    <div class="photo" style="left:261px;top:207px;width:95px;height:186px;border:2px solid #d6d6d6;border-radius:8px;background:linear-gradient(180deg,#dfe6df 55%,#fff 56%)" role="img" aria-label="Phone screen showing a map and business listing card"></div>
    <div class="foot-logo"><span class="mark"></span><span class="name">Quillmont Care Associates</span></div>
    <div class="page-no">01</div>
  </section>

  <section class="page" style="left:962px;top:1283px">
    <div class="band"></div><p class="band-title">30 Days to<br>Value Report</p><div class="band-rule"></div>
    <h2 class="title"><span class="hl">Content</span><br>And SEO</h2>
    <div class="photo" style="left:218px;top:77px;width:139px;height:108px;background:linear-gradient(135deg,#3c3f45,#6e7178 55%,#2a2c31)" role="img" aria-label="Laptop with content marketing chart overlay"></div>
    <p class="sub" style="top:128px">Content Published</p>
    <p class="bracket" style="top:142px">[List blog titles or link URLs here.]</p>
    <p class="sub" style="top:180px">SEO Progress</p>
    <ul class="list wide" style="top:194px">
      <li>Initial keyword tracking launched</li>
      <li>On-page SEO and internal linking completed</li>
      <li>Foundational ranking movement observed (if applicable)</li>
      <li>Pillar &amp; Cluster Content Calendar created — outlining key topics, publishing cadence, and interlinking structure for long-term SEO growth</li>
    </ul>
    <p class="sub" style="top:284px">Next Steps</p>
    <ul class="list" style="top:298px">
      <li>Continue publishing cluster blogs weekly</li>
      <li>Begin interlinking to new service pages</li>
    </ul>
    <div class="foot-logo"><span class="mark"></span><span class="name">Quillmont Care Associates</span></div>
    <div class="page-no">01</div>
  </section>

  <section class="page" style="left:120px;top:1864px">
    <div class="band"></div><p class="band-title">30 Days to<br>Value Report</p><div class="band-rule"></div>
    <h2 class="title"><span class="hl">Citation Listings</span><br>And Backlink Strategy</h2>
    <p class="sub" style="top:133px">Optimizations Completed</p>
    <ul class="list" style="top:147px">
      <li>Core directories completed (Findwell, Seekbay, Orchardmaps, Reviewly, etc.)</li>
      <li>Industry-specific and regional listings submitted</li>
      <li>NAP (Name–Address–Phone) consistency audit completed</li>
    </ul>
    <p class="sub" style="top:209px">Backlink Work:</p>
    <ul class="list" style="top:223px">
      <li>Foundational backlinks placed</li>
      <li>Tier-1 authority outreach plan initiated</li>
      <li>Competitor link gap opportunities identified</li>
    </ul>
    <div class="photo" style="left:222px;top:195px;width:135px;height:140px;background:radial-gradient(ellipse at 55% 55%,#cfd6ea,#eef1f8 55%,#fff 75%)" role="img" aria-label="Illustration of chess pieces beside a bar chart on a board"></div>
    <p class="sub" style="top:285px">Next Steps:</p>
    <ul class="list" style="top:299px">
      <li>Continue monthly citation expansion</li>
      <li>Launch next wave of backlink outreach</li>
    </ul>
    <div class="foot-logo"><span class="mark"></span><span class="name">Quillmont Care Associates</span></div>
    <div class="page-no">01</div>
  </section>

  <section class="page" style="left:541px;top:1864px">
    <div class="band"></div><p class="band-title">30 Days to<br>Value Report</p><div class="band-rule"></div>
    <h2 class="title"><span class="hl">Tracking</span><br>&amp; Reporting</h2>
    <p class="sub" style="top:133px">Optimizations Completed</p>
    <ul class="list" style="top:147px">
      <li>Metricly and Findwell Console connected</li>
      <li>Call tracking and form submissions live</li>
      <li>Conversion goals configured</li>
      <li>Dashboard access shared</li>
    </ul>
    <p class="sub cap" style="top:229px">Next Steps:</p>
    <ul class="list" style="top:243px">
      <li>Monitor traffic and lead source data</li>
      <li>Review conversion metrics monthly</li>
    </ul>
    <p class="sub" style="top:227px;left:189px">Next Steps:</p>
    <ul class="list" style="top:241px;left:189px">
      <li>Continue monthly citation expansion</li>
      <li>Launch next wave of backlink outreach</li>
    </ul>
    <svg class="abs" style="left:0;top:280px" width="379" height="150" viewBox="0 280 379 150" font-family="Poppins,sans-serif" font-size="7.5" fill="#fff">
      <g>
        <path d="M48 421 V331 a10 10 0 0 1 20 0 V421 Z" fill="var(--navy)"/>
        <path d="M81 421 V351 a10 10 0 0 1 20 0 V421 Z" fill="var(--gold)"/>
        <path d="M114 421 V313 a10 10 0 0 1 20 0 V421 Z" fill="var(--teal)"/>
        <path d="M147 421 V368 a10 10 0 0 1 20 0 V421 Z" fill="var(--gold)"/>
        <path d="M180 421 V300 a10 10 0 0 1 20 0 V421 Z" fill="var(--navy)"/>
        <path d="M213 421 V339 a10 10 0 0 1 20 0 V421 Z" fill="var(--gold)"/>
        <path d="M246 421 V353 a10 10 0 0 1 20 0 V421 Z" fill="var(--teal)"/>
        <path d="M279 421 V368 a10 10 0 0 1 20 0 V421 Z" fill="var(--gold)"/>
        <path d="M310 421 V346 a10 10 0 0 1 20 0 V421 Z" fill="var(--navy)"/>
      </g>
      <g>
        <text transform="translate(61 417) rotate(-90)">$1000.00</text>
        <text transform="translate(94 417) rotate(-90)">$1000.00</text>
        <text transform="translate(127 417) rotate(-90)">$1000.00</text>
        <text transform="translate(160 417) rotate(-90)">$10.00</text>
        <text transform="translate(193 417) rotate(-90)">$2000.00</text>
        <text transform="translate(226 417) rotate(-90)">$1500.00</text>
        <text transform="translate(259 417) rotate(-90)">$1800.00</text>
        <text transform="translate(292 417) rotate(-90)">$9.00</text>
        <text transform="translate(323 417) rotate(-90)">$800.00</text>
      </g>
      <line x1="27" y1="422" x2="350" y2="422" stroke="var(--navy)" stroke-width="1.5"/>
    </svg>
    <div class="foot-logo"><span class="mark"></span><span class="name">Quillmont Care Associates</span></div>
    <div class="page-no">01</div>
  </section>

  <section class="page" style="left:962px;top:1864px">
    <div class="band"></div><p class="band-title">30 Days to<br>Value Report</p><div class="band-rule"></div>
    <h2 class="title"><span class="hl">What’s Next</span><br>Days 31–60</h2>
    <p class="sub" style="top:133px">Optimizations Completed</p>
    <ul class="list" style="top:147px">
      <li>Continue backlink outreach and citation expansion</li>
      <li>Publish next wave of blog content</li>
      <li>Drive organic traffic growth via SEO</li>
      <li>Launch paid campaigns (if applicable)</li>
      <li>Review analytics data and optimize for conversions</li>
    </ul>
    <p class="sub" style="top:338px">Notes &amp; Recommendations</p>
    <p class="para" style="top:353px">The foundation is in place. The next phase focuses on growth, visibility, and conversions. We’re excited about the direction and look forward to building on this momentum.</p>
    <p class="para" style="top:384px"><b style="font-weight:600">Prepared by:</b> Dana Whitfield<br>Head of Client Success | Quillmont Care Associates</p>
    <div class="foot-logo"><span class="mark"></span><span class="name">Quillmont Care Associates</span></div>
    <div class="page-no">01</div>
  </section>

</main>
</body>
</html>
```